Rocket business card

Modern business card design, use of color is good with clean space too.

Things to include on card:

Quote: I add fuel to your optometry practice

- Eyewear Sales
- Admin Duties
- Revenue Collection
- Leadership
- Tech Adoption
- COGS Reduction
- Product Sourcing
-Medical Growth

Dalton Vessey, CEO
Glint Harbor
Text Me! 847-302-1964
dalton@glintharbor.example

```html
<!DOCTYPE html>
<html lang="en">
<head>
<meta charset="utf-8">
<title>Glint Harbor — Business Card</title>
<link href="https://fonts.googleapis.com/css2?family=Open+Sans:ital,wght@0,400;0,600;0,700;1,700&display=swap" rel="stylesheet">
<style>
  :root {
    --page: #141414;
    --card: #232323;
    --ink: #f2f2f2;
    --muted: #d8d8d8;
    --faint: #2f2f2f;
    --red: #e8401c;
    --orange: #f7941d;
    --accent: #f26a1b;
  }
  * { box-sizing: border-box; margin: 0; padding: 0; }
  html, body {
    width: 1200px; height: 900px; overflow: hidden;
    background: var(--page);
    font-family: "Open Sans", Arial, sans-serif;
  }
  .sheet {
    width: 1200px; height: 900px;
    display: flex; flex-direction: column; align-items: center; justify-content: center;
    gap: 44px;
  }
  .card {
    position: relative;
    width: 600px; height: 343px;
    background: var(--card);
    overflow: hidden;
    box-shadow: 0 18px 40px rgba(0,0,0,.55);
  }
  .card__edge {
    position: absolute; left: 0; right: 0; bottom: 0; height: 6px;
    background: linear-gradient(90deg, var(--red), var(--orange));
  }

  /* Front */
  .brand {
    position: absolute; left: 40px; top: 142px;
    width: 250px;
    display: flex; align-items: center; gap: 12px;
  }
  .brand__dot {
    width: 46px; height: 46px; border-radius: 50%; flex: none;
    background: linear-gradient(135deg, var(--red), var(--orange));
  }
  .brand__name {
    font-weight: 600; font-size: 22px; letter-spacing: 1px;
    color: var(--ink); text-transform: uppercase; white-space: nowrap;
  }
  .divider {
    position: absolute; left: 318px; top: 88px; width: 2px; height: 150px;
    background: linear-gradient(180deg, var(--red), var(--orange));
  }
  .contact {
    position: absolute; left: 340px; top: 96px; color: var(--ink);
  }
  .contact__name {
    font-weight: 700; font-style: italic; font-size: 26px;
    color: var(--accent); text-transform: uppercase; letter-spacing: .5px;
    line-height: 1.1; white-space: nowrap;
  }
  .contact__role { font-size: 16px; margin: 2px 0 14px; }
  .contact__line {
    display: flex; align-items: center; gap: 8px;
    font-size: 16px; line-height: 1.65; white-space: nowrap;
  }
  .contact__line svg { width: 14px; height: 14px; flex: none; }

  /* Back */
  .back__mark {
    position: absolute; right: 44px; top: 52px;
    display: flex; align-items: center; gap: 16px;
  }
  .back__dot {
    width: 70px; height: 70px; border-radius: 50%;
    background: var(--faint);
  }
  .back__name {
    font-weight: 600; font-size: 40px; letter-spacing: 2px;
    color: var(--faint); text-transform: uppercase; white-space: nowrap;
  }
  .back__copy {
    position: absolute; left: 44px; right: 44px; bottom: 44px;
  }
  .tagline {
    font-weight: 700; font-style: italic; font-size: 17px;
    color: var(--accent); text-transform: uppercase; letter-spacing: .3px;
    margin-bottom: 6px;
  }
  .services { font-size: 15px; color: var(--muted); line-height: 1.55; }
  .services b { color: var(--accent); font-weight: 700; padding: 0 4px; }
</style>
</head>
<body>
<main class="sheet">

  <section class="card card--front" aria-label="Business card front">
    <div class="brand">
      <span class="brand__dot"></span>
      <span class="brand__name">Glint Harbor</span>
    </div>
    <div class="divider"></div>
    <div class="contact">
      <p class="contact__name">Dalton Vessey</p>
      <p class="contact__role">CEO</p>
      <p class="contact__line">
        <svg viewBox="0 0 24 24"><path fill="#f26a1b" d="M6.6 10.8a15.1 15.1 0 0 0 6.6 6.6l2.2-2.2c.3-.3.7-.4 1-.2 1.1.4 2.3.6 3.6.6.6 0 1 .4 1 1V20c0 .6-.4 1-1 1A17 17 0 0 1 3 4c0-.6.4-1 1-1h3.5c.6 0 1 .4 1 1 0 1.3.2 2.5.6 3.6.1.3 0 .7-.2 1z"/></svg>
        847-302-1964
      </p>
      <p class="contact__line">
        <svg viewBox="0 0 24 24"><path fill="#f26a1b" d="M2 5h20v14H2z"/><path fill="none" stroke="#232323" stroke-width="2" d="M2 5l10 8 10-8"/></svg>
        dalton@glintharbor.example
      </p>
      <p class="contact__line">
        <svg viewBox="0 0 24 24"><circle cx="12" cy="12" r="10" fill="#f26a1b"/><path fill="none" stroke="#232323" stroke-width="1.6" d="M2 12h20M12 2c3 3 3 17 0 20M12 2c-3 3-3 17 0 20"/></svg>
        www.glintharbor.example
      </p>
    </div>
    <div class="card__edge"></div>
  </section>

  <section class="card card--back" aria-label="Business card back">
    <div class="back__mark">
      <span class="back__dot"></span>
      <span class="back__name">Glint Harbor</span>
    </div>
    <div class="back__copy">
      <p class="tagline">I add fuel to your optometry practice</p>
      <p class="services">
        Eyewear Sales<b>•</b>Admin Duties<b>•</b>Revenue Collection<b>•</b>Leadership<br>
        Tech Adoption<b>•</b>COGS Reduction<b>•</b>Product Sourcing<b>•</b>Medical Growth
      </p>
    </div>
    <div class="card__edge"></div>
  </section>

</main>
</body>
</html>
```